K & D A/C Compressors' Business Card

Hello,

I need someone to create a new business card for my business. The name of my Business is: K & D A/C Compressors. I sell automotive air conditioning parts (a/c parts). I would like the business card to incorporate my logo, and to have an automotive feel to it. It is important that the business card feel like it is coming from an automotive parts business.

I already have a logo, which I will provide.

Thanks.
Updates

Project Deadline Extended Reason: I feel like extending the deadline until October 9, 2017, will allow for more time to design the business card. Thank you for your understanding. Added Monday, October 2, 2017

Target Market(s)

Consumers who need automotive a/c parts, and auto mechanics.

Industry/Entity Type

Automotive

Contact Information for Business Card

Business name: K & D A/C Compressors
Business Address: 48207 Southwest 36th Street, Coral Dunes, Florida 30917
Telephone: 305-472-1390
Fax: To be provided once I choose your design.
Website: www.kdcoolunits.example
Email: support@kdcoolunits.example
Names: To be provided once I choose your design.

Font styles to use
Sans Serif

Colors

Designer to choose colors to be used in the design.

Requirements
Must have
• The business card must include all of the "Business Card Details" and the logo I have uploaded.

```html
<!DOCTYPE html>
<html lang="en">
<head>
<meta charset="utf-8">
<title>K &amp; D A/C Compressors – Business Card</title>
<link rel="stylesheet" href="https://fonts.googleapis.com/css2?family=Lato:wght@400;700&display=swap">
<style>
  :root {
    --stage: #2e2e30;
    --brand-blue: #0a9fe0;
    --brand-grey: #b2b2b2;
    --paper: #ffffff;
    --ink: #1a1a1a;
  }
  * { box-sizing: border-box; margin: 0; padding: 0; }
  html, body { width: 1200px; height: 900px; overflow: hidden; }
  body {
    background: var(--stage);
    font-family: "Lato", Arial, sans-serif;
    position: relative;
  }
  .card {
    position: absolute;
    left: 250px;
    width: 700px;
    height: 400px;
    overflow: hidden;
  }
  .card--front { top: 30px; background: var(--brand-blue); color: var(--paper); }
  .card--back { top: 470px; background: var(--paper); }

  .front-brand {
    position: absolute;
    top: 120px; left: 0; right: 0;
    text-align: center;
    font-weight: 700;
    color: var(--paper);
    line-height: 1.05;
  }
  .front-brand .brand-initials { display: block; font-size: 68px; letter-spacing: 2px; }
  .front-brand .brand-line { display: block; font-size: 40px; letter-spacing: 1px; }
  .front-web {
    position: absolute;
    bottom: 48px; left: 0; right: 0;
    text-align: center;
    font-size: 15px;
    letter-spacing: 2px;
  }

  .back-brand {
    position: absolute;
    top: 30px; left: 60px;
    font-weight: 700;
    color: var(--brand-grey);
    line-height: 1.05;
  }
  .back-brand .brand-initials { display: block; font-size: 52px; letter-spacing: 2px; }
  .back-brand .brand-line { display: block; font-size: 30px; letter-spacing: 1px; }

  .holder { position: absolute; top: 148px; left: 60px; }
  .holder-name { font-size: 26px; font-weight: 700; color: var(--brand-blue); line-height: 1.2; }
  .holder-role { font-size: 16px; color: var(--ink); }

  .bands { position: absolute; left: 0; top: 0; width: 700px; height: 400px; }

  .contact {
    position: absolute;
    top: 226px; left: 400px;
    color: var(--paper);
    font-size: 17px;
    line-height: 1.3;
  }
  .contact-address { margin-bottom: 10px; }
  .contact-list { list-style: none; }
  .contact-list li { display: flex; align-items: center; gap: 10px; margin-bottom: 2px; }
  .contact-icon { width: 15px; height: 15px; flex: none; fill: var(--paper); }
</style>
</head>
<body>

<section class="card card--front" aria-label="Business card front">
  <div class="front-brand">
    <span class="brand-initials">K &amp; D</span>
    <span class="brand-line">A/C Compressors</span>
  </div>
  <p class="front-web">www.kdcoolunits.example</p>
</section>

<section class="card card--back" aria-label="Business card back">
  <svg class="bands" viewBox="0 0 700 400" aria-hidden="true">
    <polygon fill="var(--brand-grey)" points="0,226 700,146 700,156 0,236"/>
    <polygon fill="var(--brand-blue)" points="0,248 700,168 700,400 0,400"/>
  </svg>

  <div class="back-brand">
    <span class="brand-initials">K &amp; D</span>
    <span class="brand-line">A/C Compressors</span>
  </div>

  <div class="holder">
    <p class="holder-name">Tobin Hallard</p>
    <p class="holder-role">Manager</p>
  </div>

  <div class="contact">
    <p class="contact-address">48207 Southwest 36th Street<br>Coral Dunes, Florida 30917</p>
    <ul class="contact-list">
      <li>
        <svg class="contact-icon" viewBox="0 0 24 24" aria-label="Phone"><path d="M6.6 10.8c1.4 2.8 3.8 5.1 6.6 6.6l2.2-2.2c.3-.3.7-.4 1-.2 1.1.4 2.3.6 3.6.6.6 0 1 .4 1 1V20c0 .6-.4 1-1 1C10.6 21 3 13.4 3 4c0-.6.4-1 1-1h3.5c.6 0 1 .4 1 1 0 1.3.2 2.5.6 3.6.1.3 0 .7-.2 1z"/></svg>
        <span>305-472-1390</span>
      </li>
      <li>
        <svg class="contact-icon" viewBox="0 0 24 24" aria-label="Fax"><path d="M7 3h10v4H7z M4 8h16a2 2 0 0 1 2 2v6h-4v5H6v-5H2v-6a2 2 0 0 1 2-2zm4 8v3h8v-3z"/></svg>
        <span>305-472-1391</span>
      </li>
      <li>
        <svg class="contact-icon" viewBox="0 0 24 24" aria-label="Email"><path d="M2 5h20v14H2z M3 6l9 7 9-7" stroke="#0a9fe0" stroke-width="1.5"/></svg>
        <span>support@kdcoolunits.example</span>
      </li>
      <li>
        <svg class="contact-icon" viewBox="0 0 24 24" aria-label="Website"><circle cx="12" cy="12" r="10"/><path d="M2 12h20M12 2c3 3 3 17 0 20M12 2c-3 3-3 17 0 20" stroke="#0a9fe0" stroke-width="1.5" fill="none"/></svg>
        <span>www.kdcoolunits.example</span>
      </li>
    </ul>
  </div>
</section>

</body>
</html>
```